SHG business cards

design a business card

(Generators . Lighting Towers . De-watering Pumps . Compressors) put under the logo please. my details are Marek Oyelaran (Director) 0461527308 silverpinehaulgroup@postvane.com

```html
<!DOCTYPE html>
<html lang="en">
<head>
<meta charset="UTF-8">
<title>Silverpine Haul Group — Business Card</title>
<link rel="stylesheet" href="https://fonts.googleapis.com/css2?family=Poppins:wght@300;400;600&family=Lato:wght@400&display=swap">
<style>
  :root {
    --paper: #ffffff;
    --ink: #0a0a0a;
    --gold: #e0a43a;
    --gold-deep: #c8841f;
    --gold-light: #f5c05a;
    --steel: #8c8c8c;
    --watermark-warm: #fdf1e0;
    --watermark-cool: #ececec;
  }
  * { margin: 0; padding: 0; box-sizing: border-box; }
  html, body {
    width: 1200px;
    height: 718px;
    overflow: hidden;
    background: var(--paper);
  }
  .card {
    position: relative;
    width: 1200px;
    height: 718px;
    background: var(--paper);
    font-family: "Poppins", sans-serif;
    color: var(--ink);
    overflow: hidden;
  }
  .brand {
    position: absolute;
    top: 0;
    left: 0;
    width: 1200px;
    text-align: center;
  }
  .brand-mark {
    position: absolute;
    top: 44px;
    left: 555px;
    width: 90px;
    height: 90px;
    background: var(--gold);
  }
  .brand-name {
    position: absolute;
    top: 150px;
    left: 0;
    width: 1200px;
    font-family: "Poppins", sans-serif;
    font-weight: 600;
    font-size: 44px;
    line-height: 56px;
    letter-spacing: 1px;
    color: var(--gold);
  }
  .brand-services {
    position: absolute;
    top: 232px;
    left: 0;
    width: 1200px;
    font-family: "Lato", sans-serif;
    font-size: 18.5px;
    color: var(--ink);
  }
  .divider {
    position: absolute;
    top: 288px;
    left: 0;
    width: 1200px;
    height: 3px;
    background: linear-gradient(90deg, var(--gold-light), var(--gold-deep) 50%, var(--gold-light));
  }
  .backdrop-mark {
    position: absolute;
    top: 354px;
    left: 366px;
    width: 772px;
    height: 364px;
    background: linear-gradient(90deg, var(--watermark-warm) 0%, var(--watermark-warm) 45%, var(--watermark-cool) 100%);
    opacity: 0.8;
  }
  .person {
    position: absolute;
    left: 136px;
    top: 410px;
  }
  .person-name {
    font-weight: 600;
    font-size: 61px;
    line-height: 76px;
    letter-spacing: -0.5px;
  }
  .person-role {
    font-weight: 300;
    font-size: 40px;
    line-height: 46px;
    letter-spacing: 2px;
    margin-left: 2px;
  }
  .contact {
    position: absolute;
    top: 559px;
    display: flex;
    align-items: center;
  }
  .contact-phone { left: 132px; }
  .contact-email { left: 484px; }
  .contact-icon {
    width: 58px;
    height: 58px;
    flex: none;
  }
  .contact-text {
    font-weight: 600;
    font-size: 26px;
    letter-spacing: 0.5px;
    margin-left: 20px;
  }
  .contact-email .contact-text { margin-left: 18px; }
</style>
</head>
<body>
  <main class="card">
    <header class="brand">
      <span class="brand-mark"></span>
      <div class="brand-name">SILVERPINE HAUL GROUP</div>
      <p class="brand-services">Generators . Lighting Towers . De-watering Pumps . Compressors</p>
    </header>

    <div class="divider"></div>

    <div class="backdrop-mark" role="img" aria-label="Faint enlarged brand mark as background decoration"></div>

    <section class="person">
      <h1 class="person-name">Marek Oyelaran</h1>
      <p class="person-role">Director</p>
    </section>

    <div class="contact contact-phone">
      <svg class="contact-icon" viewBox="0 0 58 58" aria-hidden="true">
        <circle cx="29" cy="29" r="29" fill="#0a0a0a"/>
        <path d="M21 16c1-1 2.5-1 3.4.2l3 4c.7 1 .6 2.3-.3 3.1l-1.8 1.6c1.3 3 3.8 5.6 6.9 7l1.6-1.8c.8-.9 2.1-1 3.1-.3l4 3c1.2.9 1.2 2.4.2 3.4l-2 2c-1.3 1.3-3.3 1.7-5 1-7.2-2.9-12.7-8.4-15.6-15.6-.7-1.7-.3-3.7 1-5z" fill="none" stroke="#ffffff" stroke-width="2.2" stroke-linejoin="round"/>
      </svg>
      <span class="contact-text">046-152-7308</span>
    </div>

    <div class="contact contact-email">
      <svg class="contact-icon" viewBox="0 0 58 58" aria-hidden="true">
        <circle cx="29" cy="29" r="29" fill="#0a0a0a"/>
        <rect x="16" y="20" width="26" height="18" fill="none" stroke="#ffffff" stroke-width="2.2"/>
        <path d="M16 20l13 11 13-11M16 38l9.5-9M42 38l-9.5-9" fill="none" stroke="#ffffff" stroke-width="2.2" stroke-linejoin="round"/>
      </svg>
      <span class="contact-text">silverpinehaulgroup@postvane.com</span>
    </div>
  </main>
</body>
</html>
```